Business Card Design Project

I have attached the logo and the colour pallete for the branding for the company.

Creative designs for business cards are needed.

The Company is modern corporate.

Industry/Entity Type

Business

```html
<!DOCTYPE html>
<html lang="en">
<head>
<meta charset="utf-8">
<title>stepgulf business cards</title>
<link rel="stylesheet" href="https://fonts.googleapis.com/css2?family=Source+Sans+3:wght@400;600;700&display=swap">
<style>
  :root {
    --stage: #2e2825;
    --card-white: #f6f7f7;
    --purple-deep: #3f1742;
    --purple-mid: #6a2a6c;
    --orange-red: #ef4f23;
    --orange-bright: #f7911e;
    --accent: #f7941d;
    --ink-light: #ffffff;
    --ink-dark: #1e1a1a;
    --ink-grey: #444444;
    --rule-grey: #9a9a9a;
  }
  * { margin: 0; padding: 0; box-sizing: border-box; }
  html, body { width: 1200px; height: 913px; overflow: hidden; }
  body {
    background: var(--stage);
    font-family: "Source Sans 3", sans-serif;
    position: relative;
  }
  .side-label {
    position: absolute;
    color: var(--ink-light);
    font-size: 34px;
    font-weight: 400;
    line-height: 1;
  }
  .side-label--back1 { left: 945px; top: 94px; }
  .side-label--back2 { left: 128px; top: 738px; }
  .side-label--back3 { left: 951px; top: 733px; }

  .card {
    position: absolute;
    width: 464px;
    height: 264px;
    box-shadow: 0 4px 10px rgba(0,0,0,0.45);
  }
  .card--front { left: 91px; top: 146px; background: var(--card-white); }
  .card--back-purple {
    left: 583px; top: 145px;
    background: linear-gradient(90deg, var(--purple-deep) 0%, var(--purple-mid) 50%, var(--purple-deep) 100%);
  }
  .card--back-orange {
    left: 91px; top: 444px;
    background: linear-gradient(90deg, var(--orange-red) 0%, var(--orange-bright) 50%, var(--orange-red) 100%);
  }
  .card--back-white { left: 589px; top: 444px; background: var(--card-white); }

  .brand {
    position: absolute;
    left: 20px; top: 88px;
    display: flex; align-items: center; gap: 8px;
    color: var(--purple-mid);
    font-size: 46px;
    font-weight: 600;
    line-height: 1;
    letter-spacing: -1px;
  }
  .brand__dot {
    width: 14px; height: 14px; border-radius: 50%;
    background: var(--orange-red);
  }
  .name-tag {
    position: absolute;
    left: 262px; top: 99px;
    width: 202px; height: 36px;
    background: linear-gradient(180deg, var(--orange-bright), var(--orange-red));
    border-radius: 8px 0 0 8px;
    color: var(--ink-light);
    font-size: 17px;
    line-height: 36px;
    padding-left: 14px;
    box-shadow: 0 3px 4px rgba(0,0,0,0.25);
  }
  .name-tag b { font-weight: 700; }

  .contact {
    position: absolute;
    top: 107px;
    font-size: 12.5px;
    line-height: 16px;
    white-space: nowrap;
  }
  .contact b { font-weight: 700; }
  .divider {
    position: absolute;
    top: 99px;
    width: 1px;
    height: 38px;
  }
  .address {
    position: absolute;
    top: 107px;
    font-size: 12.5px;
    line-height: 16px;
    white-space: nowrap;
  }

  .card--back-purple .contact { left: 24px; color: var(--ink-light); }
  .card--back-purple .contact b { color: var(--accent); }
  .card--back-purple .divider { left: 254px; background: var(--accent); }
  .card--back-purple .address { left: 280px; color: var(--ink-light); }

  .card--back-orange .contact { left: 23px; color: var(--ink-dark); }
  .card--back-orange .divider { left: 253px; background: var(--ink-light); }
  .card--back-orange .address { left: 280px; color: var(--ink-dark); }

  .card--back-white .contact { left: 28px; color: var(--ink-grey); }
  .card--back-white .contact b { color: var(--accent); }
  .card--back-white .divider { left: 259px; background: var(--rule-grey); width: 2px; }
  .card--back-white .address { left: 286px; color: var(--ink-grey); }
</style>
</head>
<body>
  <div class="side-label side-label--back1">Back 1</div>
  <div class="side-label side-label--back2">Back 2</div>
  <div class="side-label side-label--back3">Back 3</div>

  <section class="card card--front">
    <div class="brand"><span>stepgulf</span><span class="brand__dot"></span></div>
    <div class="name-tag"><b>Yourname,</b> Director</div>
  </section>

  <section class="card card--back-purple">
    <div class="contact">
      <b>T:</b> 012.345.6789, &nbsp;<b>M:</b> 012.345.6789<br>
      <b>E:</b> info@stepgulf &nbsp; <b>www.stepgulf.com</b>
    </div>
    <div class="divider"></div>
    <div class="address">Suite 000, JS building<br>Cityname, country name</div>
  </section>

  <section class="card card--back-orange">
    <div class="contact">
      <b>T:</b> 012.345.6789, &nbsp;<b>M:</b> 012.345.6789<br>
      <b>E:</b> info@stepgulf &nbsp; <b>www.stepgulf.com</b>
    </div>
    <div class="divider"></div>
    <div class="address">Suite 000, JS building<br>Cityname, country name</div>
  </section>

  <section class="card card--back-white">
    <div class="contact">
      <b>T:</b> 012.345.6789, &nbsp;<b>M:</b> 012.345.6789<br>
      <b>E:</b> info@stepgulf &nbsp; <b>www.stepgulf.com</b>
    </div>
    <div class="divider"></div>
    <div class="address">Suite 000, JS building<br>Cityname, country name</div>
  </section>
</body>
</html>
```